Harborline Toma's Chinese/Dim Sum Restaurant Menu

Harborline Toma's is a seafood-asian fusion restaurant featuring dim sum and other classical asian fusion items.

We need a menu design that includes both our food menu and our drink menu.

Food menu: Needs to have space for descriptions of food (please just include a place holder and we will input them later). See attached for food menu items.

Drink menu: Just lists of items with prices. See attached Jade Lantern Menu- please include the same items, but rebrand for Harborline Toma's.

The menus must be able to be printed in a 4.25x11in paper.

We want something modern and contemporary. My boss likes geometrical design aspects and minimalism. So, nothing too ornate. But, it has to be different from the Jade Lantern menus. Colors can be black, red, gold or blue- but it must be able to be tied into our black and red Harborline Toma's logo. Including elements of Chinese culture, especially fishing, is a plus, but not necessary.

We also need this in ai format when we download final copy so we can edit in the future.

UPDATE: Please note, we already have a logo.

Target Market(s)

Upscale family diners

Industry/Entity Type

Chinese Food

Font styles to use
Serif
Sans Serif

Colors
0054AA
0677BA
7BADD7
CADEEF
E8F1F8
0094D4
00A9DD
6FCCEA
C7EBF8
E9F6FB
FFC000
F8CF3A
FAE287
FDF2CF
FEFAEE
EB3D1F
EC4F4E
F09395
F8D3D4
FCEDEE

Requirements
Must have
• Classic, minimalist, elegant

```html
<!DOCTYPE html>
<html lang="en">
<head>
<meta charset="utf-8">
<title>Harborline Toma's — Food Menu</title>
<link href="https://fonts.googleapis.com/css2?family=Montserrat:wght@400;600;700;800;900&display=swap" rel="stylesheet">
<style>
:root{
  --red:#eb3d1f;
  --red-soft:#ec4f4e;
  --ink:#111111;
  --grey:#8a8a8a;
  --rule:#d9d9d9;
  --paper:#ffffff;
  --stage:#eeeeee;
}
*{margin:0;padding:0;box-sizing:border-box}
html,body{width:849px;height:1200px;overflow:hidden}
body{background:var(--stage);position:relative;font-family:"Montserrat",Arial,sans-serif;color:var(--ink)}
.page{position:absolute;width:340px;height:540px;background:var(--paper);box-shadow:0 3px 10px rgba(0,0,0,.18);overflow:hidden}
.page::before{content:"";position:absolute;left:12px;top:0;bottom:0;width:2px;background:var(--red)}
.page--cover{left:88px;top:24px}
.page--dimsum{left:434px;top:24px}
.page--starters{left:72px;top:612px}
.page--mains{left:420px;top:612px}
.page-head{position:absolute;left:26px;right:16px;top:10px;display:flex;justify-content:space-between;font-size:4.5px;color:var(--grey);letter-spacing:.6px;border-bottom:.5px solid var(--rule);padding-bottom:3px}

/* cover */
.cover-brand{position:absolute;left:0;right:0;top:170px;text-align:center}
.cover-mark{width:34px;height:34px;border-radius:50%;background:var(--red);margin:0 auto 18px}
.cover-name{font-weight:900;font-size:30px;letter-spacing:1px;line-height:1}
.cover-sub{font-weight:900;font-size:30px;letter-spacing:1px;line-height:1;color:var(--ink);margin-top:2px}
.cover-icons{display:flex;justify-content:center;gap:12px;margin-top:16px}
.cover-icons span{width:16px;height:16px;border-radius:50%;background:var(--ink)}
.cover-title{margin-top:16px;color:var(--red);font-weight:800;font-size:15px;letter-spacing:3px}

/* columns */
.col{position:absolute;width:142px}
.photo{width:142px;height:92px;border-radius:4px;margin-bottom:8px}
.section-title{font-size:7.5px;font-weight:800;letter-spacing:.8px;border-bottom:.6px solid var(--ink);padding-bottom:3px;margin-bottom:6px;display:flex;justify-content:space-between}
.section-title b{color:var(--red)}
.dish{list-style:none;margin-bottom:5px}
.dish-line{display:flex;justify-content:space-between;font-size:5.5px;font-weight:700;color:var(--red);letter-spacing:.3px}
.dish-price{color:var(--ink)}
.dish-desc{font-size:4.6px;color:var(--grey);line-height:1.35;margin-top:1px;width:110px}
.section + .section{margin-top:8px}

.photo--noodles{background:radial-gradient(circle at 50% 55%,#b5652a 0,#6b3412 45%,#1a1a1a 75%)}
.photo--soup{background:radial-gradient(circle at 50% 50%,#e7c28a 0,#b57a3d 40%,#f4f4f4 75%)}
.photo--greens{background:radial-gradient(circle at 50% 50%,#7da04f 0,#4b6e2c 45%,#ffffff 75%);height:70px}
.photo--bowl{background:radial-gradient(circle at 50% 50%,#8b9a5a 0,#5c4a34 45%,#ffffff 78%)}
.photo--plate{background:radial-gradient(circle at 50% 55%,#d9a86a 0,#a87a45 40%,#f2f2f2 78%)}
.photo--cake{background:linear-gradient(180deg,#ffffff 0,#5a3b2a 40%,#3a2418 70%,#ffffff 100%)}

.closing-brand{position:absolute;right:24px;bottom:36px;width:142px;text-align:center}
.closing-brand .cover-mark{width:20px;height:20px;margin-bottom:8px}
.closing-brand .cover-name,.closing-brand .cover-sub{font-size:15px}
.closing-brand .cover-title{font-size:8px;margin-top:6px;letter-spacing:2px}
</style>
</head>
<body>

<section class="page page--cover">
  <div class="cover-brand">
    <div class="cover-mark"></div>
    <div class="cover-name">HARBORLINE</div>
    <div class="cover-sub">TOMA'S</div>
    <div class="cover-icons"><span></span><span></span><span></span></div>
    <div class="cover-title">FOOD MENU</div>
  </div>
</section>

<section class="page page--dimsum">
  <div class="page-head"><span>HARBORLINE TOMA'S</span><span>FOOD MENU</span></div>
  <div class="col" style="left:26px;top:24px">
    <div class="photo photo--noodles" role="img" aria-label="Bowl of noodles with chopsticks"></div>
    <div class="section">
      <div class="section-title"><span><b>HT</b> DIM SUM</span><span>$</span></div>
      <ul>
        <li class="dish"><div class="dish-line"><span>1.SHRIMP DUMPLING</span><span class="dish-price">6</span></div><p class="dish-desc">Description of the dish to come.</p></li>
        <li class="dish"><div class="dish-line"><span>2.PORK SHUMAI</span><span class="dish-price">6</span></div><p class="dish-desc">Description of the dish to come.</p></li>
        <li class="dish"><div class="dish-line"><span>3.CHAR SIU</span><span class="dish-price">6</span></div><p class="dish-desc">Description of the dish to come.</p></li>
        <li class="dish"><div class="dish-line"><span>4.CHIVE DUMPLING</span><span class="dish-price">6</span></div><p class="dish-desc">Description of the dish to come.</p></li>
        <li class="dish"><div class="dish-line"><span>5.CRAB RANGOON</span><span class="dish-price">7</span></div><p class="dish-desc">Description of the dish to come.</p></li>
        <li class="dish"><div class="dish-line"><span>6.TURNIP CAKE</span><span class="dish-price">5</span></div><p class="dish-desc">Description of the dish to come.</p></li>
        <li class="dish"><div class="dish-line"><span>7.RICE ROLL</span><span class="dish-price">6</span></div><p class="dish-desc">Description of the dish to come.</p></li>
        <li class="dish"><div class="dish-line"><span>8.LOTUS WRAP</span><span class="dish-price">7</span></div><p class="dish-desc">Description of the dish to come.</p></li>
        <li class="dish"><div class="dish-line"><span>9.SPRING ROLL</span><span class="dish-price">5</span></div><p class="dish-desc">Description of the dish to come.</p></li>
        <li class="dish"><div class="dish-line"><span>10.TARO PUFF</span><span class="dish-price">6</span></div><p class="dish-desc">Description of the dish to come.</p></li>
        <li class="dish"><div class="dish-line"><span>11.EGG TART</span><span class="dish-price">5</span></div><p class="dish-desc">Description of the dish to come.</p></li>
        <li class="dish"><div class="dish-line"><span>12.CHICKEN FEET</span><span class="dish-price">6</span></div><p class="dish-desc">Description of the dish to come.</p></li>
        <li class="dish"><div class="dish-line"><span>13.PAN BUN</span><span class="dish-price">6</span></div><p class="dish-desc">Description of the dish to come.</p></li>
        <li class="dish"><div class="dish-line"><span>14.BEAN CURD</span><span class="dish-price">6</span></div><p class="dish-desc">Description of the dish to come.</p></li>
      </ul>
    </div>
  </div>
  <div class="col" style="left:182px;top:24px">
    <div class="photo photo--soup" role="img" aria-label="Bowl of seafood soup"></div>
    <div class="section">
      <div class="section-title"><span><b>HT</b> SOUP</span><span>$</span></div>
      <ul>
        <li class="dish"><div class="dish-line"><span>1.WONTON SOUP</span><span class="dish-price">8</span></div><p class="dish-desc">Description of the dish to come.</p></li>
        <li class="dish"><div class="dish-line"><span>2.HOT SOUR</span><span class="dish-price">8</span></div><p class="dish-desc">Description of the dish to come.</p></li>
        <li class="dish"><div class="dish-line"><span>3.EGG DROP</span><span class="dish-price">7</span></div><p class="dish-desc">Description of the dish to come.</p></li>
        <li class="dish"><div class="dish-line"><span>4.SEAFOOD SOUP</span><span class="dish-price">10</span></div><p class="dish-desc">Description of the dish to come.</p></li>
        <li class="dish"><div class="dish-line"><span>5.TOFU BROTH</span><span class="dish-price">7</span></div><p class="dish-desc">Description of the dish to come.</p></li>
        <li class="dish"><div class="dish-line"><span>6.CORN SOUP</span><span class="dish-price">7</span></div><p class="dish-desc">Description of the dish to come.</p></li>
      </ul>
    </div>
    <div class="section">
      <div class="photo photo--greens" role="img" aria-label="Fresh broccoli floret"></div>
      <div class="section-title"><span>VEGGIE</span><span>$</span></div>
      <ul>
        <li class="dish"><div class="dish-line"><span>1.GARLIC GREENS</span><span class="dish-price">9</span></div><p class="dish-desc">Description of the dish to come.</p></li>
        <li class="dish"><div class="dish-line"><span>2.MAPO TOFU</span><span class="dish-price">10</span></div><p class="dish-desc">Description of the dish to come.</p></li>
        <li class="dish"><div class="dish-line"><span>3.BOK CHOY</span><span class="dish-price">9</span></div><p class="dish-desc">Description of the dish to come.</p></li>
        <li class="dish"><div class="dish-line"><span>4.EGGPLANT STEW</span><span class="dish-price">10</span></div><p class="dish-desc">Description of the dish to come.</p></li>
      </ul>
    </div>
  </div>
</section>

<section class="page page--starters">
  <div class="page-head"><span>HARBORLINE TOMA'S</span><span>FOOD MENU</span></div>
  <div class="col" style="left:26px;top:26px">
    <div class="section">
      <div class="section-title"><span><b>HT</b> APPETIZERS</span><span>$</span></div>
      <ul>
        <li class="dish"><div class="dish-line"><span>1.SALT SQUID</span><span class="dish-price">9</span></div><p class="dish-desc">Description of the dish to come.</p></li>
        <li class="dish"><div class="dish-line"><span>2.FRIED WONTON</span><span class="dish-price">7</span></div><p class="dish-desc">Description of the dish to come.</p></li>
        <li class="dish"><div class="dish-line"><span>3.PORK RIBS</span><span class="dish-price">10</span></div><p class="dish-desc">Description of the dish to come.</p></li>
        <li class="dish"><div class="dish-line"><span>4.SCALLION PANCAKE</span><span class="dish-price">6</span></div><p class="dish-desc">Description of the dish to come.</p></li>
        <li class="dish"><div class="dish-line"><span>5.FRIED CALAMARI</span><span class="dish-price">9</span></div><p class="dish-desc">Description of the dish to come.</p></li>
        <li class="dish"><div class="dish-line"><span>6.SESAME SHRIMP</span><span class="dish-price">10</span></div><p class="dish-desc">Description of the dish to come.</p></li>
        <li class="dish"><div class="dish-line"><span>7.CHICKEN WINGS</span><span class="dish-price">9</span></div><p class="dish-desc">Description of the dish to come.</p></li>
        <li class="dish"><div class="dish-line"><span>8.LETTUCE WRAPS</span><span class="dish-price">9</span></div><p class="dish-desc">Description of the dish to come.</p></li>
        <li class="dish"><div class="dish-line"><span>9.CUCUMBER SALAD</span><span class="dish-price">6</span></div><p class="dish-desc">Description of the dish to come.</p></li>
        <li class="dish"><div class="dish-line"><span>10.EDAMAME BOWL</span><span class="dish-price">5</span></div><p class="dish-desc">Description of the dish to come.</p></li>
        <li class="dish"><div class="dish-line"><span>11.CRISPY TOFU</span><span class="dish-price">7</span></div><p class="dish-desc">Description of the dish to come.</p></li>
        <li class="dish"><div class="dish-line"><span>12.SHRIMP TOAST</span><span class="dish-price">8</span></div><p class="dish-desc">Description of the dish to come.</p></li>
        <li class="dish"><div class="dish-line"><span>13.JELLYFISH SALAD</span><span class="dish-price">9</span></div><p class="dish-desc">Description of the dish to come.</p></li>
        <li class="dish"><div class="dish-line"><span>14.SEAWEED SALAD</span><span class="dish-price">6</span></div><p class="dish-desc">Description of the dish to come.</p></li>
        <li class="dish"><div class="dish-line"><span>15.PEPPER PRAWNS</span><span class="dish-price">12</span></div><p class="dish-desc">Description of the dish to come.</p></li>
        <li class="dish"><div class="dish-line"><span>16.SMOKED FISH</span><span class="dish-price">11</span></div><p class="dish-desc">Description of the dish to come.</p></li>
      </ul>
    </div>
  </div>
  <div class="col" style="left:182px;top:24px">
    <div class="photo photo--bowl" role="img" aria-label="Bowl of sauteed beef and greens"></div>
    <div class="section">
      <div class="section-title"><span><b>HT</b> SAUTEED</span><span>$</span></div>
      <ul>
        <li class="dish"><div class="dish-line"><span>1.KUNG PAO</span><span class="dish-price">14</span></div><p class="dish-desc">Description of the dish to come.</p></li>
        <li class="dish"><div class="dish-line"><span>2.BLACK BEAN</span><span class="dish-price">14</span></div><p class="dish-desc">Description of the dish to come.</p></li>
        <li class="dish"><div class="dish-line"><span>3.GINGER FISH</span><span class="dish-price">16</span></div><p class="dish-desc">Description of the dish to come.</p></li>
        <li class="dish"><div class="dish-line"><span>4.HONEY WALNUT</span><span class="dish-price">16</span></div><p class="dish-desc">Description of the dish to come.</p></li>
        <li class="dish"><div class="dish-line"><span>5.ORANGE CHICKEN</span><span class="dish-price">13</span></div><p class="dish-desc">Description of the dish to come.</p></li>
        <li class="dish"><div class="dish-line"><span>6.BEEF BROCCOLI</span><span class="dish-price">15</span></div><p class="dish-desc">Description of the dish to come.</p></li>
        <li class="dish"><div class="dish-line"><span>7.SESAME CHICKEN</span><span class="dish-price">13</span></div><p class="dish-desc">Description of the dish to come.</p></li>
        <li class="dish"><div class="dish-line"><span>8.LEMON SOLE</span><span class="dish-price">17</span></div><p class="dish-desc">Description of the dish to come.</p></li>
        <li class="dish"><div class="dish-line"><span>9.SWEET SOUR</span><span class="dish-price">13</span></div><p class="dish-desc">Description of the dish to come.</p></li>
        <li class="dish"><div class="dish-line"><span>10.MONGOLIAN BEEF</span><span class="dish-price">15</span></div><p class="dish-desc">Description of the dish to come.</p></li>
        <li class="dish"><div class="dish-line"><span>11.CASHEW SHRIMP</span><span class="dish-price">16</span></div><p class="dish-desc">Description of the dish to come.</p></li>
        <li class="dish"><div class="dish-line"><span>12.GARLIC SCALLOP</span><span class="dish-price">18</span></div><p class="dish-desc">Description of the dish to come.</p></li>
        <li class="dish"><div class="dish-line"><span>13.BASIL CLAMS</span><span class="dish-price">16</span></div><p class="dish-desc">Description of the dish to come.</p></li>
        <li class="dish"><div class="dish-line"><span>14.CURRY SQUID</span><span class="dish-price">15</span></div><p class="dish-desc">Description of the dish to come.</p></li>
      </ul>
    </div>
  </div>
</section>

<section class="page page--mains">
  <div class="page-head"><span>HARBORLINE TOMA'S</span><span>FOOD MENU</span></div>
  <div class="col" style="left:26px;top:24px">
    <div class="photo photo--plate" role="img" aria-label="Plate of fried noodles with shrimp"></div>
    <div class="section">
      <div class="section-title"><span><b>HT</b> RICE &amp; NOODLES</span><span>$</span></div>
      <ul>
        <li class="dish"><div class="dish-line"><span>1.FRIED RICE</span><span class="dish-price">11</span></div><p class="dish-desc">Description of the dish to come.</p></li>
        <li class="dish"><div class="dish-line"><span>2.LO MEIN</span><span class="dish-price">11</span></div><p class="dish-desc">Description of the dish to come.</p></li>
        <li class="dish"><div class="dish-line"><span>3.CHOW FUN</span><span class="dish-price">12</span></div><p class="dish-desc">Description of the dish to come.</p></li>
        <li class="dish"><div class="dish-line"><span>4.CRISPY NOODLE</span><span class="dish-price">12</span></div><p class="dish-desc">Description of the dish to come.</p></li>
        <li class="dish"><div class="dish-line"><span>5.SEAFOOD RICE</span><span class="dish-price">15</span></div><p class="dish-desc">Description of the dish to come.</p></li>
        <li class="dish"><div class="dish-line"><span>6.SINGAPORE NOODLE</span><span class="dish-price">12</span></div><p class="dish-desc">Description of the dish to come.</p></li>
        <li class="dish"><div class="dish-line"><span>7.PAD THAI</span><span class="dish-price">12</span></div><p class="dish-desc">Description of the dish to come.</p></li>
        <li class="dish"><div class="dish-line"><span>8.BEEF NOODLE</span><span class="dish-price">13</span></div><p class="dish-desc">Description of the dish to come.</p></li>
        <li class="dish"><div class="dish-line"><span>9.CLAYPOT RICE</span><span class="dish-price">14</span></div><p class="dish-desc">Description of the dish to come.</p></li>
        <li class="dish"><div class="dish-line"><span>10.YANG CHOW</span><span class="dish-price">12</span></div><p class="dish-desc">Description of the dish to come.</p></li>
        <li class="dish"><div class="dish-line"><span>11.DAN DAN</span><span class="dish-price">11</span></div><p class="dish-desc">Description of the dish to come.</p></li>
        <li class="dish"><div class="dish-line"><span>12.UDON BOWL</span><span class="dish-price">12</span></div><p class="dish-desc">Description of the dish to come.</p></li>
        <li class="dish"><div class="dish-line"><span>13.CONGEE BOWL</span><span class="dish-price">9</span></div><p class="dish-desc">Description of the dish to come.</p></li>
      </ul>
    </div>
  </div>
  <div class="col" style="left:182px;top:24px">
    <div class="photo photo--cake" role="img" aria-label="Slice of layered chocolate cake"></div>
    <div class="section">
      <div class="section-title"><span><b>HT</b> SWEET &amp; DESSERT</span><span>$</span></div>
      <ul>
        <li class="dish"><div class="dish-line"><span>1.MANGO PUDDING</span><span class="dish-price">6</span></div><p class="dish-desc">Description of the dish to come.</p></li>
        <li class="dish"><div class="dish-line"><span>2.SESAME BALL</span><span class="dish-price">5</span></div><p class="dish-desc">Description of the dish to come.</p></li>
        <li class="dish"><div class="dish-line"><span>3.RED BEAN</span><span class="dish-price">5</span></div><p class="dish-desc">Description of the dish to come.</p></li>
        <li class="dish"><div class="dish-line"><span>4.EGG CUSTARD</span><span class="dish-price">6</span></div><p class="dish-desc">Description of the dish to come.</p></li>
        <li class="dish"><div class="dish-line"><span>5.ALMOND JELLY</span><span class="dish-price">6</span></div><p class="dish-desc">Description of the dish to come.</p></li>
      </ul>
    </div>
  </div>
  <div class="closing-brand">
    <div class="cover-mark"></div>
    <div class="cover-name">HARBORLINE</div>
    <div class="cover-sub">TOMA'S</div>
    <div class="cover-title">FOOD MENU</div>
  </div>
</section>

</body>
</html>
```